Build a Web page - Dovin Pratchell Homes, LLC - a custom home builder

We are a custom home builder in Wisconsin. Need a basic web page with a home page, About Us, Contact info, Gallery, and Testimonials page. Gallery will probably have sub-pages and each will have about ten pictures or less. I already own the domain and have web hosting through Wix, I just need the site built. Once the page is built I should be able to do the upkeep on it myself. If I need to add pictures or whatever.
Updates

Project Deadline Extended
Reason: I am still looking through designs and will select soon - thank you!

Target Market(s)

Gen X and Millennials who are looking to build a home. Custom built homes - not generic spec homes.

Industry/Entity Type

Home Builder

Number of Pages Required

5+ page

Font styles to use
Sans Serif

Colors
ffffff
ec1f27
000000
9d9d9d

Requirements
Must have
• I have no idea if I want coded or in coded. I'm not sure of the difference and why I would want one over the other.
Nice to have
• We like the following colors - red, black, gray, white.
Should not have
• not a big fan of clip art like hammers, tape measures, etc. Must look professional.

```html
<!DOCTYPE html>
<html lang="en">
<head>
<meta charset="utf-8">
<title>Dovin Pratchell Homes, LLC</title>
<link href="https://fonts.googleapis.com/css2?family=Abel&family=Open+Sans:ital,wght@0,400;0,600;0,700;1,400&display=swap" rel="stylesheet">
<style>
:root{
  --red:#b0080d;
  --red-bright:#ec1f27;
  --black:#000;
  --ink:#222;
  --gray:#9d9d9d;
  --light:#f1f1f1;
  --white:#fff;
  --footer:#1f1f1f;
}
*{margin:0;padding:0;box-sizing:border-box}
html,body{width:1200px;height:2703px;overflow:hidden}
body{position:relative;background:var(--white);font-family:"Open Sans",sans-serif;color:var(--ink)}
.abs{position:absolute}
.heading{font-family:"Abel",sans-serif}

/* header */
.site-header{left:0;top:0;width:1200px;height:130px;background:var(--black)}
.brand{left:0;top:0;width:300px;height:130px}
.brand-name{left:40px;top:36px;width:200px;font-family:"Open Sans",sans-serif;font-weight:700;font-size:20px;line-height:26px;color:var(--red)}
.social{display:flex;gap:6px}
.social span{width:32px;height:32px;border:1px solid #444;display:block}
.header-social{left:314px;top:14px}
.header-rule{left:300px;top:62px;width:790px;height:1px;background:#333}
.contact-chip{top:14px;display:flex;gap:12px;color:var(--white)}
.contact-chip .ico{width:30px;height:30px;background:#333;display:flex;align-items:center;justify-content:center}
.contact-chip b{display:block;font-weight:400;font-size:13px}
.contact-chip small{display:block;font-size:10px;color:#ccc}
.main-nav{left:472px;top:84px;display:flex;gap:0;font-size:14px;color:var(--white)}
.main-nav a{color:inherit;text-decoration:none;margin-right:40px}
.btn-quote{left:973px;top:74px;width:115px;height:38px;background:var(--red);color:var(--white);font-size:13px;display:flex;align-items:center;justify-content:center}

/* hero */
.hero{left:0;top:130px;width:1200px;height:598px;background:linear-gradient(180deg,#6a6a66 0%,#4e4d49 45%,#3a4233 78%,#2e3328 100%)}
.hero-arrow{top:370px}
.hero-panel{left:112px;top:256px;width:479px;height:330px;background:var(--red);color:var(--white);padding:26px 28px}
.hero-panel h1{font-family:"Open Sans",sans-serif;font-weight:400;font-size:30px;line-height:36px}
.hero-panel .lead{font-size:12.5px;line-height:23px;text-transform:uppercase;color:#f4c9c9;margin-top:6px}
.hero-panel ul{list-style:none;margin-top:14px}
.hero-panel li{font-size:13px;line-height:29px;display:flex;align-items:center;gap:10px}
.btn-outline{display:inline-flex;align-items:center;justify-content:center;border:1px solid var(--white);color:var(--white);font-size:13px}
.hero-panel .btn-outline{margin-top:16px;width:117px;height:40px}

/* section titles */
.section-title{left:0;width:1200px;text-align:center;font-size:30px}
.title-bar{width:70px;height:2px;background:var(--red);left:565px}

/* about */
.about-copy{left:112px;top:842px;width:976px;text-align:center;font-size:11.5px;line-height:20px;color:#444}
.feature{top:920px;width:300px}
.feature h3{position:absolute;left:45px;top:4px;font-size:16px;font-weight:600;color:var(--red)}
.feature p{position:absolute;left:48px;top:36px;width:215px;font-size:11px;line-height:19px;color:#555}

/* gallery */
.gallery{left:0;top:1054px;width:1200px;height:746px;background:linear-gradient(135deg,#4f0f1c 0%,#6b1a2b 35%,#7b2136 55%,#5a1322 80%,#3f0d18 100%)}
.filter{top:1191px;height:40px;border:1px solid #e7c9cf;color:var(--white);font-size:13px;display:flex;align-items:center;justify-content:center}
.filter.active{background:var(--white);color:var(--red);border-color:var(--white)}
.tile{width:230px;height:177px;border:6px solid var(--white)}
.tile .photo{position:absolute;inset:0}
.tile .overlay{position:absolute;inset:8px;border:1px solid var(--red-bright);background:rgba(0,0,0,.45);color:var(--white);text-align:center;padding-top:24px}
.tile h4{font-family:"Abel",sans-serif;font-weight:400;font-size:19px;text-transform:uppercase}
.tile p{font-size:10.5px;line-height:18px;margin:10px 14px 0}
.tile .overlay.left h4{text-align:left;padding-left:6px}
.tile .bar{position:absolute;left:50%;bottom:14px;width:34px;height:2px;margin-left:-17px;background:var(--red-bright)}
.gallery-cta{left:324px;top:1716px;color:var(--white);font-size:16px;font-weight:600}
.gallery .btn-outline{}

/* testimonials */
.testimonials{left:0;top:1800px;width:1200px;height:480px;background:linear-gradient(180deg,#fff 0%,#fff 40%,#f3f3f3 100%)}
.quote-card{top:1993px;width:301px;height:218px;background:var(--white);border:2px solid #e6e6e6}
.quote-card p{position:absolute;left:20px;top:68px;width:260px;text-align:center;font-style:italic;font-size:11px;line-height:22px;color:#777}
.quote-card .rule{position:absolute;left:20px;right:20px;top:178px;height:1px;background:#ddd}
.quote-card .name{position:absolute;left:0;width:100%;top:188px;text-align:center;font-size:10.5px;color:#555}
.avatar{top:1939px}

/* footer */
.site-footer{left:0;top:2280px;width:1200px;height:423px;background:var(--footer);color:var(--white)}
.footer-col h5{font-family:"Abel",sans-serif;font-weight:400;font-size:18px;letter-spacing:.5px}
.footer-col p{font-size:11.5px;line-height:22px;color:#ccc}
.newsletter-input{left:112px;top:2443px;width:200px;height:42px;background:var(--white);color:#888;font-size:10.5px;padding:13px 10px}
.newsletter-btn{left:312px;top:2443px;width:99px;height:42px;background:var(--red);font-size:11.5px;font-weight:700;display:flex;align-items:center;justify-content:center}
.quick-menu{list-style:none;font-size:11px;line-height:27.5px;color:#ddd}
.quick-menu li::before{content:"»";margin-right:12px}
.contact-row{display:flex;gap:18px;align-items:flex-start}
.contact-row .ico{width:32px;height:32px;border:1px solid #555;display:flex;align-items:center;justify-content:center;flex:none}
.footer-rule{left:0;top:2577px;width:1200px;height:1px;background:#333}
.copyright{left:0;top:2653px;width:1200px;text-align:center;font-size:11px;color:#ccc}
</style>
</head>
<body>

<!-- header -->
<header class="abs site-header">
  <svg class="abs brand" width="300" height="130" viewBox="0 0 300 130"><polygon points="0,0 255,0 300,65 255,130 0,130" fill="#fff"/></svg>
  <div class="abs brand-name">Dovin Pratchell Homes</div>
  <div class="abs social header-social"><span></span><span></span><span></span><span></span></div>
  <div class="abs header-rule"></div>
  <div class="abs contact-chip" style="left:787px">
    <div class="ico"><svg width="16" height="12" viewBox="0 0 16 12"><rect x="0.5" y="0.5" width="15" height="11" fill="none" stroke="#bbb"/><polyline points="1,1 8,7 15,1" fill="none" stroke="#bbb"/></svg></div>
    <div><b>Email</b><small>info@domain.com</small></div>
  </div>
  <div class="abs contact-chip" style="left:953px">
    <div class="ico"><svg width="14" height="14" viewBox="0 0 24 24"><path d="M6 2l4 4-2 3c1.5 3 4 5.5 7 7l3-2 4 4-3 4C10 21 3 14 2 5z" fill="#bbb"/></svg></div>
    <div><b>Call Now</b><small>info@domain.com</small></div>
  </div>
  <nav class="abs main-nav"><a>Home</a><a>About Us</a><a>Gallery</a><a>Testimonials</a><a>Contact Info</a></nav>
  <div class="abs btn-quote">GET A QUOTE</div>
</header>

<!-- hero -->
<section class="abs hero" role="img" aria-label="Photograph of a finished two-storey custom home with lawn and young tree at dusk"></section>
<svg class="abs hero-arrow" style="left:20px" width="24" height="70" viewBox="0 0 24 70"><polyline points="22,2 2,35 22,68" fill="none" stroke="#ddd" stroke-width="2"/></svg>
<svg class="abs hero-arrow" style="left:1156px" width="24" height="70" viewBox="0 0 24 70"><polyline points="2,2 22,35 2,68" fill="none" stroke="#ddd" stroke-width="2"/></svg>
<div class="abs hero-panel">
  <h1>WELCOME TO DOVIN PRATCHELL</h1>
  <p class="lead">It is a long established fact that a reader will be distract<br>by the readable content of a page when<br>looking at its layout.</p>
  <ul>
    <li><svg width="14" height="14" viewBox="0 0 14 14"><rect x="1" y="1" width="12" height="12" fill="none" stroke="#fff" stroke-width="1.5"/><polyline points="3.5,7 6,9.5 10.5,4" fill="none" stroke="#fff" stroke-width="1.5"/></svg>Building of your Dream</li>
    <li><svg width="14" height="14" viewBox="0 0 14 14"><rect x="1" y="1" width="12" height="12" fill="none" stroke="#fff" stroke-width="1.5"/><polyline points="3.5,7 6,9.5 10.5,4" fill="none" stroke="#fff" stroke-width="1.5"/></svg>We 'll Take Care Your Opinion and Hope</li>
    <li><svg width="14" height="14" viewBox="0 0 14 14"><rect x="1" y="1" width="12" height="12" fill="none" stroke="#fff" stroke-width="1.5"/><polyline points="3.5,7 6,9.5 10.5,4" fill="none" stroke="#fff" stroke-width="1.5"/></svg>Best Architecture We have</li>
  </ul>
  <div class="btn-outline">GET A QUOTE</div>
</div>

<!-- about -->
<h2 class="abs section-title heading" style="top:762px;font-weight:400">About Us</h2>
<div class="abs title-bar" style="top:806px"></div>
<p class="abs about-copy">It is a long established fact that a reader will be distracted by the readable content of a page when looking at its layout. The point of using Lorem Ipsum is that it has a more-or-less normal<br>distribution of letters, as opposed to using 'Content here, content here.</p>

<div class="abs feature" style="left:112px">
  <svg class="abs" style="left:0;top:4px" width="34" height="28" viewBox="0 0 34 28"><rect x="1" y="4" width="30" height="22" rx="2" fill="none" stroke="#b0080d" stroke-width="2"/><path d="M4 4l18-3 2 3" fill="none" stroke="#b0080d" stroke-width="2"/><rect x="22" y="12" width="11" height="7" fill="#fff" stroke="#b0080d" stroke-width="2"/></svg>
  <h3>REASONABLE PRICE</h3>
  <p>Established fact that a readbe distracted by the readable content of a page when looking at its layout.</p>
</div>
<div class="abs feature" style="left:472px">
  <svg class="abs" style="left:0;top:0" width="34" height="36" viewBox="0 0 34 36"><circle cx="17" cy="13" r="10" fill="none" stroke="#b0080d" stroke-width="2"/><circle cx="17" cy="13" r="5" fill="none" stroke="#b0080d" stroke-width="1.5"/><polyline points="10,21 6,34 12,31 15,35 17,24" fill="none" stroke="#b0080d" stroke-width="2"/><polyline points="24,21 28,34 22,31 19,35 17,24" fill="none" stroke="#b0080d" stroke-width="2"/></svg>
  <h3>CERTIFIED ENGINEER</h3>
  <p>Established fact that a readbe distracted by the readable content of a page when looking at its layout.</p>
</div>
<div class="abs feature" style="left:831px">
  <svg class="abs" style="left:0;top:0" width="34" height="36" viewBox="0 0 34 36"><path d="M3 2h20l8 8v24H3z" fill="none" stroke="#b0080d" stroke-width="2"/><line x1="8" y1="14" x2="24" y2="14" stroke="#b0080d" stroke-width="2"/><line x1="8" y1="20" x2="24" y2="20" stroke="#b0080d" stroke-width="2"/><line x1="8" y1="26" x2="18" y2="26" stroke="#b0080d" stroke-width="2"/></svg>
  <h3>GURANTEED WORKS</h3>
  <p>Established fact that a readbe distracted by the readable content of a page when looking at its layout.</p>
</div>

<!-- gallery -->
<section class="abs gallery" role="img" aria-label="Deep maroon faceted low-poly background"></section>
<h2 class="abs section-title heading" style="top:1097px;font-weight:400;color:#fff">Project Gallery</h2>
<div class="abs title-bar" style="top:1142px;background:#fff"></div>
<div class="abs filter active" style="left:333px;width:117px">SHOW ALL</div>
<div class="abs filter" style="left:470px;width:117px">BUILDING</div>
<div class="abs filter" style="left:604px;width:117px">INTERIOR</div>
<div class="abs filter" style="left:735px;width:132px">ARCHITECTURE</div>

<div class="abs tile" style="left:112px;top:1274px"><div class="photo" role="img" aria-label="Bright interior staircase with wooden banister" style="background:linear-gradient(135deg,#d9d2c4,#a87a52 55%,#6e4a2f)"></div></div>
<div class="abs tile" style="left:360px;top:1274px"><div class="photo" role="img" aria-label="Interior with wooden staircase" style="background:linear-gradient(135deg,#5a3a26,#2a1a12)"></div><div class="overlay"><h4>Interior</h4><p>Established fact that a readbe distracted by the readable content of a page when.</p><div class="bar"></div></div></div>
<div class="abs tile" style="left:609px;top:1274px"><div class="photo" role="img" aria-label="Exterior of a two-storey house" style="background:linear-gradient(180deg,#5d6167,#3b3f3a 60%,#2d3a22)"></div><div class="overlay"><h4>Architech</h4><p>Established fact that a readbe distracted by the readable content of a page when.</p><div class="bar"></div></div></div>
<div class="abs tile" style="left:858px;top:1274px"><div class="photo" role="img" aria-label="Kitchen interior with dark wood cabinets" style="background:linear-gradient(135deg,#4a2e20,#22150f)"></div><div class="overlay"><h4>Interior</h4><p>Established fact that a readbe distracted by the readable content of a page when.</p><div class="bar"></div></div></div>

<div class="abs tile" style="left:112px;top:1472px"><div class="photo" role="img" aria-label="House under construction" style="background:linear-gradient(135deg,#5a5650,#2e2c29)"></div><div class="overlay left"><h4>Building</h4><p>Established fact that a readbe distracted by the readable content of a page when.</p><div class="bar"></div></div></div>
<div class="abs tile" style="left:360px;top:1472px"><div class="photo" role="img" aria-label="Interior with wooden staircase" style="background:linear-gradient(135deg,#5a3a26,#2a1a12)"></div><div class="overlay"><h4>Interior</h4><p>Established fact that a readbe distracted by the readable content of a page when.</p><div class="bar"></div></div></div>
<div class="abs tile" style="left:609px;top:1472px"><div class="photo" role="img" aria-label="Kitchen with wooden cabinetry" style="background:linear-gradient(135deg,#5e3b25,#2a1a12)"></div><div class="overlay"><h4>Architech</h4><p>Established fact that a readbe distracted by the readable content of a page when.</p><div class="bar"></div></div></div>
<div class="abs tile" style="left:858px;top:1472px"><div class="photo" role="img" aria-label="Interior with wooden staircase" style="background:linear-gradient(135deg,#553624,#22150f)"></div><div class="overlay"><h4>Interior</h4><p>Established fact that a readbe distracted by the readable content of a page when.</p><div class="bar"></div></div></div>

<div class="abs gallery-cta">WE BUILD PROFESSIONAL AND SMART BUILDINGS</div>
<div class="abs btn-outline" style="left:760px;top:1708px;width:116px;height:40px">GET A QUOTE</div>

<!-- testimonials -->
<section class="abs testimonials" role="img" aria-label="Faint city skyline silhouette behind testimonials"></section>
<h2 class="abs section-title heading" style="top:1843px;font-weight:400;color:#111">Testimonials</h2>
<div class="abs title-bar" style="top:1890px"></div>

<div class="abs quote-card" style="left:112px"><p><b style="font-size:18px;color:#999">&ldquo;</b> Contrary to popular belief, Lorem Ipsum is not simply random text. It has roots in a piece of classical Latin literature from 45 BC, making it over 2000 years old. Richard <b style="font-size:18px;color:#555">&rdquo;</b></p><div class="rule"></div><div class="name">CUSTOMER NAME</div></div>
<div class="abs quote-card" style="left:450px"><p><b style="font-size:18px;color:#999">&ldquo;</b> Contrary to popular belief, Lorem Ipsum is not simply random text. It has roots in a piece of classical Latin literature from 45 BC, making it over 2000 years old. Richard <b style="font-size:18px;color:#555">&rdquo;</b></p><div class="rule"></div><div class="name">CUSTOMER NAME</div></div>
<div class="abs quote-card" style="left:787px"><p><b style="font-size:18px;color:#999">&ldquo;</b> Contrary to popular belief, Lorem Ipsum is not simply random text. It has roots in a piece of classical Latin literature from 45 BC, making it over 2000 years old. Richard <b style="font-size:18px;color:#555">&rdquo;</b></p><div class="rule"></div><div class="name">CUSTOMER NAME</div></div>

<svg class="abs avatar" style="left:214px" width="96" height="104" viewBox="0 0 96 104"><polygon points="48,2 94,27 94,77 48,102 2,77 2,27" fill="#e2e2e2"/></svg>
<svg class="abs avatar" style="left:552px" width="96" height="104" viewBox="0 0 96 104"><polygon points="48,2 94,27 94,77 48,102 2,77 2,27" fill="#e2e2e2"/></svg>
<svg class="abs avatar" style="left:889px" width="96" height="104" viewBox="0 0 96 104"><polygon points="48,2 94,27 94,77 48,102 2,77 2,27" fill="#e2e2e2"/></svg>

<!-- footer -->
<footer class="abs site-footer"></footer>
<svg class="abs" style="left:0;top:2280px" width="1200" height="40" viewBox="0 0 1200 40"><path d="M0 0H1200L820 0Q700 30 600 30Q500 30 380 0Z" fill="#f3f3f3"/><circle cx="600" cy="22" r="18" fill="#b0080d"/><polyline points="593,25 600,18 607,25" fill="none" stroke="#fff" stroke-width="2"/></svg>

<div class="abs footer-col" style="left:112px;top:2356px;width:300px;color:#fff">
  <h5>NEWSLETTER SIGNUP</h5>
  <p style="margin-top:10px">Contrary to popular belief, Lorem Ipsum is not simply random text.</p>
</div>
<div class="abs newsletter-input">Enter your Email id</div>
<div class="abs newsletter-btn" style="color:#fff">SUBSCRIBE</div>

<div class="abs footer-col" style="left:497px;top:2356px;color:#fff">
  <h5>QUICK MENU</h5>
  <ul class="quick-menu" style="margin-top:8px"><li>Home</li><li>About Us</li><li>Gallery</li><li>Testimonials</li><li>Contact</li></ul>
</div>

<div class="abs footer-col" style="left:730px;top:2356px;width:360px;color:#fff">
  <h5>CONTACT US</h5>
  <div class="contact-row" style="margin-top:14px">
    <div class="ico"><svg width="14" height="14" viewBox="0 0 24 24"><path d="M6 2l4 4-2 3c1.5 3 4 5.5 7 7l3-2 4 4-3 4C10 21 3 14 2 5z" fill="#aaa"/></svg></div>
    <div><div style="font-size:14px">0123 456 789, &nbsp; 0123 456 789</div><div style="font-size:9.5px;color:#2a8fd6">Please Contact Us</div></div>
  </div>
  <div class="contact-row" style="margin-top:12px">
    <div class="ico"><svg width="16" height="12" viewBox="0 0 16 12"><rect x="0.5" y="0.5" width="15" height="11" fill="none" stroke="#aaa"/><polyline points="1,1 8,7 15,1" fill="none" stroke="#aaa"/></svg></div>
    <div style="font-size:11.5px;line-height:22px;color:#ddd">yourname@domain.com<br>your2ndname@domain.com</div>
  </div>
  <div class="contact-row" style="margin-top:10px">
    <div class="ico"><svg width="12" height="16" viewBox="0 0 12 16"><path d="M6 0a6 6 0 0 0-6 6c0 4.5 6 10 6 10s6-5.5 6-10a6 6 0 0 0-6-6z" fill="#aaa"/><circle cx="6" cy="6" r="2.2" fill="#1f1f1f"/></svg></div>
    <div style="font-size:11.5px;line-height:20px;color:#ddd">Built by the award , home builder, No. : 215<br>Street main Highway, 478521</div>
  </div>
</div>

<div class="abs footer-rule"></div>
<div class="abs social" style="left:518px;top:2606px"><span></span><span></span><span></span><span></span></div>
<div class="abs copyright">Copy Right © All Rights Reserved . 2017</div>

</body>
</html>
```